Promo pages for me as a speaker who has expert advice for educators and as a consultant..

I need a promo page (or two) designed for introducing myself and my services as a speaker. I want to introduce myself to local radio, newspaper, school districts, churches and TV stations as a possible guest. The promo pages have to include my first book, Lanterns over the Schoolyard which is available on Rivvenmart.com and describes my true experience as an inner-city high school teacher. It encapsulates educational strategies which can empower teachers and provide guidelines for greater success in the classroom setting; and consequently, for greater individual student motivation and achievement. My second book, Quiet Notes to Nana (also available on Rivvenmart.com), is a compilation of inspirational true stories to uplift and encourage the reader. Both are Christian based. I want the public (also churches) to be more aware of educators and their difficult work. I want teachers to know there are strategies that work in establishing a better learning environment, especially within our diverse culture and advanced technology influence.

Target Market(s)

local newspapers, radio stations, TV news stations, school districts and churches

Font styles to use
Serif
Sans Serif
Script

Colors

Designer to choose colors to be used in the design.

Requirements
Must have
• Pictures of both books, my website info/link TallMeadowAdvising.com, a picture of me. What I offer: encouragement for teachers, strategies that work for teachers and individuals, families, ministries and businesses. Bullet phrases stating how I can help. I will list the bullet phrases for each promo page to the graphic designer when needed.
Nice to have
• I would like to see two kinds of promo sheets. One with focus on education. Another with focus on Biblical truths as foundation for success in the public workplace.

```html
<!DOCTYPE html>
<html lang="en">
<head>
<meta charset="utf-8">
<title>Nora L. Hartwell – Speaker Promo Sheets</title>
<link href="https://fonts.googleapis.com/css2?family=Arimo:ital,wght@0,400;0,700;1,400&family=Kaushan+Script&family=Tinos:ital,wght@0,400;0,700;1,400&display=swap" rel="stylesheet">
<style>
:root{
  --plum:#4b1b5e;
  --plum-deep:#3a1149;
  --lavender:#e6deec;
  --lime:#a8c14b;
  --lime-bright:#cde06a;
  --cream:#fbf9ee;
  --paper:#ffffff;
  --stage:#f1f1f1;
  --ink:#2a2a2a;
  --star:#f39a1e;
  --sans:'Arimo',Arial,sans-serif;
  --serif:'Tinos','Times New Roman',serif;
  --script:'Kaushan Script',cursive;
}
*{margin:0;padding:0;box-sizing:border-box}
html,body{width:1200px;height:1000px;overflow:hidden;background:var(--stage)}
.canvas{position:relative;width:1200px;height:1000px}
.sheet{position:absolute;top:125px;width:568px;height:733px;background:var(--paper);overflow:hidden;box-shadow:0 6px 14px rgba(0,0,0,.25)}
.sheet--education{left:18px}
.sheet--ministry{left:614px}
.sheet__shapes{position:absolute;inset:0}
.abs{position:absolute}
.brand{display:flex;align-items:center;gap:10px;font-family:var(--serif);font-size:16px;line-height:1.1}
.brand__mark{width:30px;height:30px;background:var(--lime-bright);flex:none}
.script{font-family:var(--script);font-weight:400}
.stars{display:flex;gap:2px}
.stars svg{width:13px;height:13px}
.contact{font-family:var(--sans);font-size:10px;display:flex;align-items:center;gap:8px;color:var(--ink)}
.contact__icon{width:11px;height:11px;border-radius:50%;background:var(--plum);display:inline-flex;align-items:center;justify-content:center}
.contact__icon svg{width:7px;height:7px}
.market{font-family:var(--sans);font-weight:700;font-size:17px;color:var(--ink);letter-spacing:.2px}

/* education sheet */
.edu-brand{left:283px;top:30px;color:#fff;font-size:15px}
.edu-name{left:285px;top:108px;width:270px;height:42px;color:var(--plum);font-size:29px;text-align:center;line-height:42px}
.edu-roles{left:300px;top:157px;width:250px;text-align:center;color:#fff;font-family:var(--sans);font-size:14px;letter-spacing:.3px}
.edu-headline{left:290px;top:203px;width:262px;text-align:right;color:#fff;font-size:22px}
.edu-sub{left:300px;top:240px;width:252px;text-align:right;color:#fff;font-family:var(--sans);font-size:10px;letter-spacing:.2px}
.edu-story{left:280px;top:262px;width:272px;text-align:right;color:#fff;font-family:var(--sans);font-size:9.8px;line-height:12.8px}
.edu-learn{left:26px;top:410px;color:#fff;font-size:21px}
.edu-learn-rule{left:28px;top:450px;width:220px;height:2px;background:var(--lime-bright)}
.edu-list{left:26px;top:465px;width:232px;list-style:none;color:#fff;font-family:var(--sans);font-style:italic;font-size:9.4px;line-height:12.2px;white-space:nowrap}
.edu-list li::before{content:"• "}
.edu-book{left:264px;top:408px;width:280px;height:228px}
.edu-book__front{position:absolute;left:0;top:0;width:140px;height:228px;background:linear-gradient(180deg,#e8eef0 0%,#bcd0d6 45%,#2f6b5a 100%);box-shadow:2px 3px 6px rgba(0,0,0,.35)}
.edu-book__back{position:absolute;left:148px;top:6px;width:132px;height:218px;background:linear-gradient(180deg,#f2f3ef,#cdd8d4);box-shadow:2px 3px 6px rgba(0,0,0,.35)}
.edu-book__title{position:absolute;left:6px;top:12px;width:128px;text-align:center;font-family:var(--serif);font-size:13px;line-height:14px;color:#1d3e4a;letter-spacing:.5px}
.edu-book__author{position:absolute;left:6px;top:180px;width:128px;text-align:center;font-family:var(--serif);font-size:10px;color:#fff}
.edu-book-cta{left:26px;top:648px;color:var(--plum);font-size:21px}
.edu-phone{left:28px;top:687px}
.edu-mail{left:28px;top:703px}
.edu-market{left:452px;top:662px}
.edu-stars{left:455px;top:686px}

/* ministry sheet */
.min-brand{left:23px;top:27px;color:var(--ink);font-size:19px}
.min-brand .brand__mark{width:36px;height:36px}
.min-name{left:26px;top:112px;color:var(--plum);font-size:30px}
.min-roles{left:26px;top:168px;font-family:var(--serif);font-weight:700;font-size:14px;line-height:17px;color:var(--ink);letter-spacing:.5px}
.min-headline{left:26px;top:222px;color:var(--plum);font-size:20px}
.min-sub{left:26px;top:254px;font-family:var(--serif);font-size:12px;color:var(--ink);letter-spacing:.3px}
.min-story{left:21px;top:281px;width:278px;text-align:justify;font-family:var(--serif);font-size:11.3px;line-height:13.9px;color:var(--ink)}
.min-books{left:14px;top:494px;width:280px;height:220px}
.min-book{position:absolute;top:0;width:132px;height:220px;background:linear-gradient(180deg,#f4efe6 0%,#d9c3a3 45%,#b48d64 100%);box-shadow:2px 3px 6px rgba(0,0,0,.35)}
.min-book--a{left:0}
.min-book--b{left:146px}
.min-book__title{position:absolute;left:6px;top:58px;width:120px;text-align:center;font-family:var(--script);font-size:17px;line-height:19px;color:#3a2a22}
.min-book__author{position:absolute;left:6px;top:198px;width:120px;text-align:center;font-family:var(--serif);font-size:8px;color:#3a2a22;letter-spacing:.5px}
.min-topics{right:17px;top:478px;color:var(--plum);font-size:22px}
.min-list{right:17px;top:513px;list-style:none;text-align:right;font-family:var(--serif);font-style:italic;font-size:10.6px;line-height:12.2px;color:var(--ink)}
.min-list li::after{content:" •"}
.min-rule{left:320px;top:648px;width:232px;height:1px;background:#777}
.min-market{left:318px;top:672px}
.min-stars{left:320px;top:694px}
.min-book-cta{right:30px;top:655px;color:var(--plum);font-size:21px}
.min-phone{right:17px;top:690px}
.min-mail{right:17px;top:705px}
</style>
</head>
<body>
<div class="canvas">

  <section class="sheet sheet--education">
    <svg class="sheet__shapes" viewBox="0 0 568 733" width="568" height="733">
      <rect width="568" height="733" fill="var(--plum)"/>
      <circle cx="110" cy="175" r="190" fill="var(--lavender)"/>
      <circle cx="110" cy="175" r="178" fill="#d8cdbf" role="img" aria-label="Portrait photo of the speaker"/>
      <path d="M0 645 Q300 668 568 628 V733 H0 Z" fill="var(--paper)"/>
      <rect y="723" width="568" height="10" fill="var(--plum)"/>
      <path d="M272 112 Q400 100 560 108 L556 150 Q420 146 280 154 Z" fill="var(--lime-bright)"/>
    </svg>

    <div class="abs brand edu-brand"><span class="brand__mark"></span>Tall Meadow Advising, LLC</div>
    <h1 class="abs script edu-name">Nora L. Hartwell</h1>
    <p class="abs edu-roles">AUTHOR. TEACHER. SPEAKER.</p>
    <h2 class="abs script edu-headline">Teaching and Loving It!</h2>
    <p class="abs edu-sub">DISCOVERING YOUR STRENGTHS FOR SUCCESS</p>
    <p class="abs edu-story">As a late bloomer at the age of 40, I began a new kind of education as I stepped into the massive foyer of the first high school in the heart of Kansas City. Although I obtained a master’s degree in education, I lacked the skills needed for this environment. I was far from perfect, but my on-the-job training created strategies which brought success for my students as well as providing empowerment for me and others. I want teachers to know there are approaches that work in establishing a better learning environment, especially within our diverse culture and advanced technological influence.</p>

    <h2 class="abs script edu-learn">What You Will Learn:</h2>
    <div class="abs edu-learn-rule"></div>
    <ul class="abs edu-list">
      <li>Lessons on What Not to do in the Classroom</li>
      <li>Teaching the Unreachable Student</li>
      <li>What I Needed to Know, but Didn’t Learn in College</li>
      <li>Choosing the Most Important Thing</li>
      <li>How to Keep Your Blood Pressure in Check</li>
      <li>Building Positive Student Identity</li>
      <li>Investing in Your Students’ Future</li>
      <li>Flexibility Works Wonders</li>
      <li>Classroom Strategies for Student Success</li>
      <li>Handling the Stress of Standardized Testing</li>
      <li>Dealing with Dishonest Students</li>
      <li>Knowing You Made a Difference</li>
      <li>And much more. . .</li>
    </ul>

    <div class="abs edu-book" role="img" aria-label="Front and back cover of the book Lanterns over the Schoolyard">
      <div class="edu-book__front">
        <div class="edu-book__title">LANTERNS OVER THE SCHOOLYARD</div>
        <div class="edu-book__author">Nora L. Hartwell</div>
      </div>
      <div class="edu-book__back"></div>
    </div>

    <h2 class="abs script edu-book-cta">To Book Nora</h2>
    <p class="abs contact edu-phone"><span class="contact__icon"><svg viewBox="0 0 10 10"><path d="M2 1 L4 1 L4.6 3 L3.5 3.8 Q4.5 5.8 6.2 6.5 L7 5.4 L9 6 V8 Q5 9 2 5 Q1 3 2 1Z" fill="#fff"/></svg></span>555-014-2290</p>
    <p class="abs contact edu-mail"><span class="contact__icon"><svg viewBox="0 0 10 10"><rect x="1.5" y="2.5" width="7" height="5" fill="#fff"/><path d="M1.5 2.5 L5 5.5 L8.5 2.5" stroke="var(--plum)" stroke-width=".8" fill="none"/></svg></span>tallmeadow@inboxly.com</p>
    <p class="abs market edu-market">Rivvenmart</p>
    <div class="abs stars edu-stars">
      <svg viewBox="0 0 10 10"><path d="M5 .5 6.3 3.6 9.6 3.8 7 6 7.9 9.4 5 7.6 2.1 9.4 3 6 .4 3.8 3.7 3.6Z" fill="var(--star)"/></svg>
      <svg viewBox="0 0 10 10"><path d="M5 .5 6.3 3.6 9.6 3.8 7 6 7.9 9.4 5 7.6 2.1 9.4 3 6 .4 3.8 3.7 3.6Z" fill="var(--star)"/></svg>
      <svg viewBox="0 0 10 10"><path d="M5 .5 6.3 3.6 9.6 3.8 7 6 7.9 9.4 5 7.6 2.1 9.4 3 6 .4 3.8 3.7 3.6Z" fill="var(--star)"/></svg>
      <svg viewBox="0 0 10 10"><path d="M5 .5 6.3 3.6 9.6 3.8 7 6 7.9 9.4 5 7.6 2.1 9.4 3 6 .4 3.8 3.7 3.6Z" fill="var(--star)"/></svg>
      <svg viewBox="0 0 10 10"><path d="M5 .5 6.3 3.6 9.6 3.8 7 6 7.9 9.4 5 7.6 2.1 9.4 3 6 .4 3.8 3.7 3.6Z" fill="var(--star)"/></svg>
    </div>
  </section>

  <section class="sheet sheet--ministry">
    <svg class="sheet__shapes" viewBox="0 0 568 733" width="568" height="733">
      <rect width="568" height="733" fill="var(--lime)"/>
      <path d="M300 0 H568 V440 Q430 470 300 458 Z" fill="var(--plum)"/>
      <circle cx="445" cy="250" r="180" fill="var(--paper)"/>
      <circle cx="445" cy="250" r="172" fill="#d8cdbf" role="img" aria-label="Portrait photo of the speaker"/>
      <path d="M300 470 Q440 480 568 448 V733 H300 Z" fill="var(--paper)"/>
      <rect y="723" width="568" height="10" fill="var(--plum)"/>
      <path d="M0 108 H270 A27 27 0 0 1 270 162 H0 Z" fill="var(--cream)"/>
    </svg>

    <div class="abs brand min-brand"><span class="brand__mark"></span>Tall Meadow<br>Advising, LLC</div>
    <h1 class="abs script min-name">Nora L. Hartwell</h1>
    <p class="abs min-roles">AUTHOR | TEACHER | MINISTER<br>SPEAKER | CONSULTANT</p>
    <h2 class="abs script min-headline">Equipped and Empowered!</h2>
    <p class="abs min-sub">DISCOVERING YOUR DISTINCTIVE JOURNEY</p>
    <p class="abs min-story">Nora has traveled nationally and internationally as a speaker, teacher and consultant since 2013. As a licensed minister, she has nurtured and supported individuals, couples and other ministries through effective counseling. She is the author of Lanterns over the Schoolyard, which demonstrates God’s faithfulness during her years of teaching and consulting within the inner-city high schools. Quiet Notes to Nana is a compilation of her articles published online. They are inspirational messages of God’s intimate love toward us which encourage and exhort through scripture, stories and Biblical truths. Nora desires that people truly know God’s intense love for them and that they come to realize their identity and empowerment through Christ.</p>

    <div class="abs min-books" role="img" aria-label="Two copies of the book Quiet Notes to Nana">
      <div class="min-book min-book--a"><div class="min-book__title">Quiet Notes to Nana</div><div class="min-book__author">BY NORA L. HARTWELL</div></div>
      <div class="min-book min-book--b"><div class="min-book__title">Quiet Notes to Nana</div><div class="min-book__author">BY NORA L. HARTWELL</div></div>
    </div>

    <h2 class="abs script min-topics">Topics</h2>
    <ul class="abs min-list">
      <li>Knowing Your Identity</li>
      <li>Becoming Free from the Past</li>
      <li>Finding Your Journey</li>
      <li>Sustaining Successful Relationships</li>
      <li>Attaining Effective Ministry and Business Strategies</li>
      <li>Empowering Others</li>
      <li>Obtaining and Keeping Unity for Your Team</li>
      <li>Restoring Vision and Purpose</li>
      <li>Implementing a Solid Foundation and Framework</li>
      <li>And much more</li>
    </ul>
    <div class="abs min-rule"></div>
    <p class="abs market min-market">Rivvenmart</p>
    <div class="abs stars min-stars">
      <svg viewBox="0 0 10 10"><path d="M5 .5 6.3 3.6 9.6 3.8 7 6 7.9 9.4 5 7.6 2.1 9.4 3 6 .4 3.8 3.7 3.6Z" fill="var(--star)"/></svg>
      <svg viewBox="0 0 10 10"><path d="M5 .5 6.3 3.6 9.6 3.8 7 6 7.9 9.4 5 7.6 2.1 9.4 3 6 .4 3.8 3.7 3.6Z" fill="var(--star)"/></svg>
      <svg viewBox="0 0 10 10"><path d="M5 .5 6.3 3.6 9.6 3.8 7 6 7.9 9.4 5 7.6 2.1 9.4 3 6 .4 3.8 3.7 3.6Z" fill="var(--star)"/></svg>
      <svg viewBox="0 0 10 10"><path d="M5 .5 6.3 3.6 9.6 3.8 7 6 7.9 9.4 5 7.6 2.1 9.4 3 6 .4 3.8 3.7 3.6Z" fill="var(--star)"/></svg>
      <svg viewBox="0 0 10 10"><path d="M5 .5 6.3 3.6 9.6 3.8 7 6 7.9 9.4 5 7.6 2.1 9.4 3 6 .4 3.8 3.7 3.6Z" fill="var(--star)"/></svg>
    </div>
    <h2 class="abs script min-book-cta">To Book Nora</h2>
    <p class="abs contact min-phone">555-014-2290<span class="contact__icon"><svg viewBox="0 0 10 10"><path d="M2 1 L4 1 L4.6 3 L3.5 3.8 Q4.5 5.8 6.2 6.5 L7 5.4 L9 6 V8 Q5 9 2 5 Q1 3 2 1Z" fill="#fff"/></svg></span></p>
    <p class="abs contact min-mail">tallmeadow@inboxly.com<span class="contact__icon"><svg viewBox="0 0 10 10"><rect x="1.5" y="2.5" width="7" height="5" fill="#fff"/><path d="M1.5 2.5 L5 5.5 L8.5 2.5" stroke="var(--plum)" stroke-width=".8" fill="none"/></svg></span></p>
  </section>

</div>
</body>
</html>
```